High-end executive coaching group needs a 2 page digital flyer

We need a 2 page digital flyer for a high end leadership coaching offering for global leaders in healthcare. The flyer will advertise a new service (an elite senior leadership coaching group) for senior leaders in the healthcare industry from around the world.
The flyer should be upmarket, professional and minimalist in style to meet the expectations of my professional market (very senior doctors and executives).
The design should be based on my existing logo and brand, see my landing page: www.lantavereadvisory.com
The key elements needed are
1) An editable PDF which we can update as we revise the specific details of the offering. The text and draft design for this is attached.
2) The banner image should be high quality but abstract. It can be based on the landing page of my website (the two ripple effects) but does not need to strictly adhere to this.
3) The logo placement of the Lantavere Advisory delta sign should be discreet so that it does not dominate
4) The small logos of our professional accrediting organisations should be discreetly placed at the end and should not dominate. They might work best as mono icons in a footer (e.g. blue on a white background, or white on blue.
5) Please find enclosed a previous flyer as an example of a similar style we have used for more junior professionals. The design worked quite well, although we now need a more upmarket version for our senior executives.
Updates

Please note this design specifically needs to use existing branding and images from my website: lantavereadvisory.com. We are definitely not looking for stock "leadership team" images for this high-end brochure.

Target Market(s)

Senior global leaders in the healthcare industry

Industry/Entity Type

Leading business schools & Healthcare industry.

Font styles to use
Other font styles liked:
• Operetta (selective use for heading) and Sofia Pro (body text)

Colors
0054AA
0677BA
7BADD7
CADEEF
E8F1F8

Requirements
Must have
• Clean minimalist and high professionally look that directly speaks to the interests and perspectives of senior leader leaders in healthcare. It also needs very clear call to action sections
Nice to have
• Effective presentation of the two bios and photographs. These need to look impressive, but should not dominate.
Should not have
• Loud and bold colours, large use of logos.

```html
<!DOCTYPE html>
<html lang="en">
<head>
<meta charset="utf-8">
<title>Analytic Coaching Group for Senior Leaders – Flyer</title>
<link href="https://fonts.googleapis.com/css2?family=Playfair+Display:wght@600;700&family=Outfit:wght@300;400;500&display=swap" rel="stylesheet">
<style>
:root{
  --navy:#0054AA;
  --blue:#0677BA;
  --sky:#7BADD7;
  --mist:#CADEEF;
  --ice:#E8F1F8;
  --stage:#2F7BB5;
  --ink:#3a4654;
  --white:#ffffff;
}
*{box-sizing:border-box;margin:0;padding:0}
html,body{width:1200px;height:800px;overflow:hidden}
body{background:var(--stage);font-family:"Outfit",sans-serif;color:var(--ink);position:relative}
.page{position:absolute;top:18px;width:540px;height:764px;background:var(--white);overflow:hidden}
.page--front{left:40px}
.page--back{left:620px}
.abs{position:absolute}
.bar{display:block;width:22px;height:3px;background:var(--navy);margin-bottom:5px}
.brand{left:28px;top:44px;display:flex;align-items:center;gap:6px;font-family:"Playfair Display",serif;font-weight:600;font-size:11px;color:var(--navy)}
.brand-mark{width:10px;height:10px;border-radius:50%;background:var(--navy)}
.hero-title{left:34px;top:128px;font-family:"Playfair Display",serif;font-weight:700;font-size:33px;line-height:1.12;color:var(--white)}
.hero-title .soft{color:var(--mist)}
.tagline{left:34px;top:312px;width:300px;font-size:9px;line-height:1.35;color:var(--navy)}
.offer-title{left:34px;top:346px;font-family:"Playfair Display",serif;font-weight:600;font-size:16px;color:var(--navy)}
.intro{left:34px;top:372px;width:470px;font-size:8.6px;line-height:1.4}
.intro p+p{margin-top:6px}
.section-title{font-family:"Playfair Display",serif;font-weight:600;font-size:13px;color:var(--navy);margin-bottom:8px}
.benefits{left:34px;top:448px;width:240px}
.benefit{display:flex;gap:7px;font-size:8.4px;line-height:1.35;margin-bottom:9px}
.benefit b{font-family:"Playfair Display",serif;font-weight:600;color:var(--blue)}
.tick{flex:0 0 12px;height:12px;margin-top:1px}
.quote{font-size:8.4px;line-height:1.4;position:relative;padding:4px 10px}
.quote-mark{position:absolute;font-family:"Playfair Display",serif;font-size:34px;line-height:1;color:var(--mist)}
.quote-mark--open{left:-8px;top:-6px}
.quote-mark--close{right:-2px;bottom:-20px}
.quote-by{font-size:7.5px;margin-top:8px;color:#6b7785}
.testimonial-front{left:292px;top:448px;width:210px}
.details{left:292px;top:556px;width:220px}
.details table{border-collapse:collapse;font-size:8px;line-height:1.35}
.details th{text-align:right;font-weight:400;padding-right:5px;vertical-align:top;border-right:1px solid var(--navy);white-space:nowrap}
.details td{padding-left:5px;vertical-align:top}
.contact{display:flex;align-items:center;gap:5px;font-size:8px;color:var(--white)}
.contact svg{width:10px;height:10px}
.phone{font-size:15px;color:var(--white);display:flex;align-items:center;gap:8px}
.phone svg{width:14px;height:14px}
.get-in-touch{left:300px;top:690px;font-size:11px;color:var(--navy)}
.back-title{left:0;top:40px;width:540px;text-align:center;font-family:"Playfair Display",serif;font-weight:700;font-size:14.5px;line-height:1.25;color:var(--navy)}
.portrait{width:150px;height:140px;border-radius:28px 28px 0 0;background:linear-gradient(160deg,var(--mist),var(--sky))}
.name-tag{height:18px;background:var(--navy);color:var(--white);font-size:9px;display:flex;align-items:center;justify-content:center;width:150px}
.bio{font-size:7.9px;line-height:1.38;text-align:justify;width:220px}
.engage{left:34px;top:418px;width:230px}
.engage .section-title{font-size:11px;line-height:1.3}
.question{display:flex;gap:7px;font-size:8.2px;line-height:1.35;margin-bottom:10px}
.question svg{flex:0 0 7px;height:7px;margin-top:2px}
.cta{left:296px;top:426px;width:220px}
.cta h3{font-family:"Playfair Display",serif;font-weight:600;font-size:12px;color:var(--blue)}
.cta p{font-size:8.2px;line-height:1.35}
.booking{left:296px;top:478px;width:230px}
.booking h3{font-family:"Playfair Display",serif;font-weight:600;font-size:12px;color:var(--ink);margin-bottom:3px}
.booking a{display:block;font-family:"Playfair Display",serif;font-size:10.5px;color:var(--navy);text-decoration:none;line-height:1.45}
.badges{left:34px;top:596px;display:flex;gap:10px;align-items:center}
.badge{width:28px;height:16px;background:var(--mist);border-radius:3px}
.badge--round{width:16px;border-radius:50%}
.testimonial-back{left:300px;top:584px;width:200px;font-size:7.4px}
</style>
</head>
<body>

<section class="page page--front" aria-label="Flyer page one">
  <svg class="abs" style="left:0;top:0" width="540" height="320" viewBox="0 0 540 320" aria-hidden="true">
    <defs>
      <linearGradient id="peak" x1="0" y1="0" x2="1" y2="1">
        <stop offset="0" stop-color="#dfeef2"/>
        <stop offset="0.55" stop-color="#9fc4cf"/>
        <stop offset="1" stop-color="#4f7f93"/>
      </linearGradient>
    </defs>
    <rect x="0" y="18" width="180" height="12" fill="var(--sky)"/>
    <polygon points="180,18 192,18 200,30 188,30" fill="var(--sky)"/>
    <polygon points="196,18 206,18 214,30 204,30" fill="var(--mist)"/>
  </svg>
  <svg class="abs" style="left:0;top:0" width="540" height="320" viewBox="0 0 540 320" role="img" aria-label="Abstract snow-capped mountain peak in pale teal tones">
    <polygon points="205,0 540,0 540,230 350,230" fill="url(#peak)"/>
  </svg>
  <svg class="abs" style="left:0;top:0" width="540" height="320" viewBox="0 0 540 320" aria-hidden="true">
    <polygon points="14,98 258,98 410,296 14,296" fill="var(--blue)"/>
    <polygon points="258,98 300,98 452,296 410,296" fill="var(--navy)" opacity="0.85"/>
    <polygon points="350,230 540,230 540,268 380,268" fill="var(--navy)"/>
    <polygon points="306,150 338,150 380,206 348,206" fill="var(--sky)" opacity="0.6"/>
  </svg>

  <div class="abs brand"><span class="brand-mark"></span>Lantavere Advisory</div>

  <h1 class="abs hero-title">Elevate <span class="soft">and</span><br>Ignite <span class="soft">your</span><br>Leadership</h1>

  <p class="abs tagline">Transformative conversations for senior healthcare leaders. Unlock purpose, engage authentically and amplify your leadership impact.</p>

  <h2 class="abs offer-title">Analytic Coaching Group for Senior Leaders</h2>
  <div class="abs intro">
    <p>As a senior leader in healthcare, you're constantly navigating challenges.<br>But where do you turn for authentic connections, reflection and personal growth?</p>
    <p>Rethink your leadership assumptions and approach challenges with fresh creativity.<br>Secure your spot in our exclusive Analytic Coaching Group and ignite your leadership potential.</p>
  </div>

  <div class="abs benefits">
    <span class="bar"></span>
    <h3 class="section-title">Benefits to you</h3>
    <div class="benefit"><svg class="tick" viewBox="0 0 12 12"><circle cx="6" cy="6" r="6" fill="var(--navy)"/><path d="M3.2 6.2l1.9 1.9 3.7-3.9" stroke="#fff" stroke-width="1.4" fill="none"/></svg><span><b>Transformative conversations:</b> Engage in discussions that spark innovative leadership</span></div>
    <div class="benefit"><svg class="tick" viewBox="0 0 12 12"><circle cx="6" cy="6" r="6" fill="var(--sky)"/><path d="M3.2 6.2l1.9 1.9 3.7-3.9" stroke="#fff" stroke-width="1.4" fill="none"/></svg><span><b>Peer insights:</b> Harness fresh insights from peers, enhancing your decision-making and effectiveness</span></div>
    <div class="benefit"><svg class="tick" viewBox="0 0 12 12"><circle cx="6" cy="6" r="6" fill="var(--navy)"/><path d="M3.2 6.2l1.9 1.9 3.7-3.9" stroke="#fff" stroke-width="1.4" fill="none"/></svg><span><b>Reimagined leadership:</b> Channel your creativity and redefine your leadership, personally and professionally</span></div>
    <div class="benefit"><svg class="tick" viewBox="0 0 12 12"><circle cx="6" cy="6" r="6" fill="var(--sky)"/><path d="M3.2 6.2l1.9 1.9 3.7-3.9" stroke="#fff" stroke-width="1.4" fill="none"/></svg><span><b>Instant 360 insights:</b> Gain real-time feedback from trusted peers to enrich your leadership</span></div>
    <div class="benefit"><svg class="tick" viewBox="0 0 12 12"><circle cx="6" cy="6" r="6" fill="var(--navy)"/><path d="M3.2 6.2l1.9 1.9 3.7-3.9" stroke="#fff" stroke-width="1.4" fill="none"/></svg><span><b>Lead authentically:</b> Develop effective strategies using the latest insights from group and leadership psychology</span></div>
  </div>

  <blockquote class="abs quote testimonial-front">
    <span class="quote-mark quote-mark--open">“</span>
    You bare your heart and share things you wouldn't under normal circumstances. You get to know each other very quickly. There's that sort of intense, shared experience that comes from speaking to each other's lives.
    <span class="quote-mark quote-mark--close">”</span>
    <p class="quote-by">Sarah, Medical Director</p>
  </blockquote>

  <div class="abs details">
    <span class="bar"></span>
    <h3 class="section-title">Secure your spot now and<br>ignite your leadership</h3>
    <table>
      <tr><th>Dates</th><td>7 February 2024 – 11 December 2024</td></tr>
      <tr><th>Time</th><td>7:30am – 8:45am (UK time)</td></tr>
      <tr><th>Commitment</th><td>Wednesdays, every 2 weeks</td></tr>
      <tr><th>Location</th><td>Connect from anywhere by Meetwell</td></tr>
      <tr><th>Cost</th><td>£3350 [UK] €3900 [Europe]<br>A$6530 [Australia]<br>Payment options available</td></tr>
    </table>
  </div>

  <p class="abs get-in-touch">Get In Touch</p>
  <svg class="abs" style="left:0;top:700px" width="540" height="64" viewBox="0 0 540 64" aria-hidden="true">
    <polygon points="0,22 230,22 248,64 0,64" fill="var(--blue)"/>
    <polygon points="240,0 254,0 276,44 262,44" fill="var(--sky)"/>
    <polygon points="260,0 272,0 294,44 282,44" fill="var(--mist)"/>
    <polygon points="290,22 540,10 540,36 300,44" fill="var(--blue)"/>
  </svg>
  <div class="abs phone" style="left:30px;top:729px">
    <svg viewBox="0 0 24 24"><path fill="#fff" d="M6.6 10.8a15 15 0 006.6 6.6l2.2-2.2a1 1 0 011-.25 11.4 11.4 0 003.6.57 1 1 0 011 1V20a1 1 0 01-1 1A17 17 0 013 4a1 1 0 011-1h3.5a1 1 0 011 1c0 1.25.2 2.45.57 3.57a1 1 0 01-.25 1z"/></svg>
    +61 3 9000 4210
  </div>
  <div class="abs contact" style="left:310px;top:718px">
    <svg viewBox="0 0 24 24"><circle cx="12" cy="12" r="10" fill="none" stroke="#fff" stroke-width="2"/><path d="M2 12h20M12 2c3 3 3 17 0 20M12 2c-3 3-3 17 0 20" fill="none" stroke="#fff" stroke-width="1.5"/></svg>
    www.lantavereadvisory.com
  </div>
  <div class="abs contact" style="left:430px;top:713px">
    <svg viewBox="0 0 24 24"><rect x="2" y="5" width="20" height="14" rx="1" fill="none" stroke="#fff" stroke-width="2"/><path d="M2 6l10 7 10-7" fill="none" stroke="#fff" stroke-width="2"/></svg>
    info@lantavereadvisory.com
  </div>
</section>

<section class="page page--back" aria-label="Flyer page two">
  <svg class="abs" style="left:0;top:0" width="540" height="36" viewBox="0 0 540 36" aria-hidden="true">
    <rect x="0" y="0" width="170" height="26" fill="var(--mist)"/>
    <polygon points="170,0 186,0 202,26 186,26" fill="var(--sky)"/>
    <polygon points="206,36 230,0 254,36" fill="var(--navy)"/>
    <polygon points="236,0 262,0 250,18" fill="var(--white)"/>
    <rect x="262" y="0" width="278" height="22" fill="var(--sky)"/>
    <rect x="262" y="22" width="278" height="12" fill="var(--navy)"/>
  </svg>

  <h2 class="abs back-title">Expertly guided by insight, academic rigour and<br>practical leadership strategies</h2>

  <svg class="abs" style="left:0;top:92px" width="540" height="170" viewBox="0 0 540 170" role="img" aria-label="Textured deep blue backdrop behind the coach portraits">
    <defs>
      <linearGradient id="band" x1="0" y1="0" x2="1" y2="1">
        <stop offset="0" stop-color="#0a6a9e"/>
        <stop offset="1" stop-color="#075a8c"/>
      </linearGradient>
    </defs>
    <rect x="14" y="0" width="512" height="170" fill="url(#band)"/>
  </svg>

  <div class="abs" style="left:70px;top:110px">
    <div class="portrait" role="img" aria-label="Portrait photograph of Prof. Daniel Hartwell"></div>
    <div class="name-tag">Prof. Daniel Hartwell</div>
  </div>
  <div class="abs" style="left:320px;top:110px">
    <div class="portrait" role="img" aria-label="Portrait photograph of Dr. Helen Marlowe"></div>
    <div class="name-tag">Dr. Helen Marlowe</div>
  </div>

  <p class="abs bio" style="left:34px;top:276px">Professor Daniel Hartwell has 30 years' experience developing leaders. An award-winning business school professor, group analyst and psychoanalytic psychotherapist, he has taught senior leadership programmes at Ashbury University, Kingsmere College and the University of Southbank. His extensive leadership experience as a national health service clinical director and consultant psychotherapist inform his work as a Corvale Coaching Guild accredited executive coach. With a PhD from Halden College, London, he is an expert in melding psychological insights with strategic organisational change.</p>
  <p class="abs bio" style="left:290px;top:276px">Dr Helen Marlowe is a renowned psychoanalyst, group analyst, consultant psychiatrist and organisational consultant in the health sector. She has 20 years of leadership within the national health service, and she was also the National Director of Therapies for the Meridian Care Group, directing therapy services across 100 UK hospitals. She holds prominent positions as Chair of the Patient Safety Group, Chair of the Working Group on the Effect of Suicide and Homicide on Psychiatrists, and Vice Chair of the Psychotherapy Faculty at the Royal Society of Psychiatry.</p>

  <div class="abs engage">
    <span class="bar"></span>
    <h3 class="section-title">Engage with global leaders, gain diverse insights and forge lasting bonds.<br>Explore questions such as:</h3>
    <div class="question"><svg viewBox="0 0 8 7"><polygon points="4,0 8,7 0,7" fill="var(--navy)"/></svg><span>What kind of leader do I aspire to be in the next chapter of my life and career?</span></div>
    <div class="question"><svg viewBox="0 0 8 7"><polygon points="4,0 8,7 0,7" fill="var(--navy)"/></svg><span>What unique qualities and actions do I offer that no one else can?</span></div>
    <div class="question"><svg viewBox="0 0 8 7"><polygon points="4,0 8,7 0,7" fill="var(--navy)"/></svg><span>How can I galvanise my personal strengths to inspire and motivate others?</span></div>
  </div>

  <div class="abs cta">
    <h3>Limited spots available.</h3>
    <p>Don't miss this unique opportunity to transform your leadership journey.</p>
  </div>

  <div class="abs booking">
    <span class="bar"></span>
    <h3>Book your free discovery call</h3>
    <a href="#">daniel@lantavereadvisory.com</a>
    <a href="#">helenmarlowe@mailbox.net</a>
    <a href="#">www.lantavereadvisory.com</a>
  </div>

  <div class="abs badges" aria-label="Accrediting organisations">
    <span class="badge badge--round"></span>
    <span class="badge"></span>
    <span class="badge"></span>
    <span class="badge"></span>
  </div>

  <blockquote class="abs quote testimonial-back">
    <span class="quote-mark quote-mark--open">“</span>
    Through this exceptional coaching, our leadership team elevated its performance to lead the hospital with greater clarity, cohesion and thoughtfulness. Not only do we provide a superior work environment for staff, but better care for our patients.
    <span class="quote-mark quote-mark--close">”</span>
    <p class="quote-by" style="text-align:center">John, CEO</p>
  </blockquote>

  <svg class="abs" style="left:0;top:690px" width="540" height="74" viewBox="0 0 540 74" aria-hidden="true">
    <polygon points="0,14 220,14 240,54 0,54" fill="var(--blue)"/>
    <polygon points="226,14 240,14 260,54 246,54" fill="var(--sky)"/>
    <polygon points="246,14 258,14 278,54 266,54" fill="var(--mist)"/>
    <polygon points="262,14 540,14 540,40 276,40" fill="var(--blue)"/>
  </svg>
  <div class="abs phone" style="left:30px;top:719px">
    <svg viewBox="0 0 24 24"><path fill="#fff" d="M6.6 10.8a15 15 0 006.6 6.6l2.2-2.2a1 1 0 011-.25 11.4 11.4 0 003.6.57 1 1 0 011 1V20a1 1 0 01-1 1A17 17 0 013 4a1 1 0 011-1h3.5a1 1 0 011 1c0 1.25.2 2.45.57 3.57a1 1 0 01-.25 1z"/></svg>
    +61 3 9000 4210
  </div>
  <div class="abs contact" style="left:296px;top:711px">
    <svg viewBox="0 0 24 24"><circle cx="12" cy="12" r="10" fill="none" stroke="#fff" stroke-width="2"/><path d="M2 12h20M12 2c3 3 3 17 0 20M12 2c-3 3-3 17 0 20" fill="none" stroke="#fff" stroke-width="1.5"/></svg>
    www.lantavereadvisory.com
  </div>
  <div class="abs contact" style="left:420px;top:711px">
    <svg viewBox="0 0 24 24"><rect x="2" y="5" width="20" height="14" rx="1" fill="none" stroke="#fff" stroke-width="2"/><path d="M2 6l10 7 10-7" fill="none" stroke="#fff" stroke-width="2"/></svg>
    info@lantavereadvisory.com
  </div>
</section>

</body>
</html>
```